Help us make a CLOVERTON impact! Saving Dogs from Kill Shelters.....

*Our mission is to save Dogs from kill shelters, and unite them with responsible families nationwide.

*We would love to incorporate sacred geometry into our message. The "Flower of Life" needs to be incorporated into this design.Earth Friendly Self-Sustainable Animal Shelter is a goal. Solar Power

*We want the professional look of exclusiveness.

*The logo/brand is not set in stone, and we welcome opinions!

***Earth Consciousness. Awareness. Love.

Peace. LOVE. Adopt. :)

I would like a sleek exclusive look, one that says WOW. This design needs to have a good energy about it. I have envisioned the front being logo only and vertical. Please have a look at our Facebook page to get a feel about what we are doing & trying to accomplish...

*ONE Side Card
**The flower of life inlay needs to be in or around of the logo.
***The following is the ONLY information I want on the card!

CLOVERTON Adoption Center

Maren Hollis

www.CLOVERTONadoptioncenter.com

(555)013-4478

FB Icon

Target Market(s)

Stable, Wealthy, Responsible Families in the Northeast.

Industry/Entity Type

Solar

Contact Information for Business Card

CLOVERTON Adoption Center, Maren Hollis, Founder/Director, 912 Birchwood Court, Fernwick Springs, KY 40927, (555)013-4478, FB Icon

Requirements
Must have
• FB icon on back.
The "Flower of Life" must be incorporated into this design.
Nice to have
• Positive Energy
Bright Colors
WOW Factor

```html
<!DOCTYPE html>
<html lang="en">
<head>
<meta charset="utf-8">
<title>CLOVERTON Adoption Center – Business Card</title>
<link rel="stylesheet" href="https://fonts.googleapis.com/css2?family=Anton&display=swap">
<style>
  :root {
    --backdrop: #4a3b2c;
    --card: #ffffff;
    --green: #1fcf1a;
    --green-deep: #0f9e12;
    --lime: #e6f53a;
    --lime-soft: #b9ec2f;
    --ink: #111111;
  }
  * { margin: 0; padding: 0; box-sizing: border-box; }
  html, body { width: 1200px; height: 1000px; overflow: hidden; }
  body {
    position: relative;
    background: var(--backdrop);
    font-family: "Anton", "Impact", sans-serif;
    color: var(--ink);
  }
  .card {
    position: absolute;
    top: 63px;
    height: 872px;
    background: var(--card);
  }
  .card--front { left: 30px; width: 562px; }
  .card--back { left: 610px; width: 560px; }
  .card__stripe { position: absolute; top: 0; bottom: 0; width: 20px; }
  .card__stripe--left { left: 0; background: linear-gradient(to bottom, var(--green-deep), var(--lime-soft) 55%, var(--lime)); }
  .card__stripe--right { right: 0; background: linear-gradient(to bottom, var(--lime), var(--lime-soft) 45%, var(--green-deep)); }

  .emblem {
    position: absolute;
    background: radial-gradient(circle closest-side at 50% 55%, #f4f86a 0%, #9fe22a 45%, #22b51b 88%, rgba(255,255,255,0) 100%);
  }
  .card--front .emblem { left: 150px; top: 99px; width: 265px; height: 290px; }
  .card--back .emblem { left: 176px; top: 55px; width: 204px; height: 224px; }

  .emblem-shadow { position: absolute; }
  .card--front .emblem-shadow { left: 137px; top: 441px; }
  .card--back .emblem-shadow { left: 167px; top: 317px; }

  .brand-name {
    position: absolute;
    left: 0; right: 0;
    text-align: center;
    color: var(--green);
    line-height: 1;
    letter-spacing: 0.5px;
  }
  .card--front .brand-name { top: 533px; font-size: 56px; }
  .card--back .brand-name { top: 387px; font-size: 42px; }

  .brand-subtitle {
    position: absolute;
    top: 434px; left: 0; right: 0;
    text-align: center;
    font-size: 25px;
    line-height: 1;
  }
  .brand-subtitle__name { color: var(--green); }

  .person { position: absolute; top: 553px; left: 0; right: 0; text-align: center; line-height: 1; }
  .person__name { color: var(--green); font-size: 38px; }
  .person__role { font-size: 24px; margin-top: 6px; }

  .contact {
    position: absolute;
    left: 78px;
    display: flex;
    align-items: center;
    gap: 18px;
    font-size: 24px;
    line-height: 34px;
  }
  .contact__badge {
    flex: none;
    width: 40px; height: 40px;
    border-radius: 50%;
    background: var(--lime);
    display: flex; align-items: center; justify-content: center;
  }
  .contact--address { top: 702px; align-items: flex-start; }
  .contact--address .contact__badge { margin-top: -2px; }
  .contact--phone { top: 776px; }
  .contact--social { top: 816px; left: 53px; gap: 12px; font-size: 24px; }
  .contact--social .contact__badge { width: 36px; height: 36px; }
</style>
</head>
<body>

  <section class="card card--front">
    <div class="card__stripe card__stripe--left"></div>
    <div class="card__stripe card__stripe--right"></div>

    <div class="emblem" role="img" aria-label="Green globe with four paw-pad toes above it, forming a paw print"></div>
    <svg class="emblem-shadow" width="276" height="44" viewBox="0 0 276 44" aria-hidden="true">
      <defs>
        <radialGradient id="shadowFront" cx="50%" cy="50%" r="50%">
          <stop offset="0" stop-color="#5c8c16"/>
          <stop offset="0.6" stop-color="#a9cf3e"/>
          <stop offset="1" stop-color="#ffffff" stop-opacity="0"/>
        </radialGradient>
      </defs>
      <ellipse cx="138" cy="22" rx="138" ry="22" fill="url(#shadowFront)"/>
    </svg>

    <h1 class="brand-name">CLOVERTON</h1>

    <p class="contact contact--social">
      <span class="contact__badge" aria-hidden="true"></span>
      <span>Friendbook.com/clovertonadoptioncentre</span>
    </p>
  </section>

  <section class="card card--back">
    <div class="card__stripe card__stripe--left"></div>
    <div class="card__stripe card__stripe--right"></div>

    <div class="emblem" role="img" aria-label="Green globe with four paw-pad toes above it, forming a paw print"></div>
    <svg class="emblem-shadow" width="212" height="34" viewBox="0 0 212 34" aria-hidden="true">
      <defs>
        <radialGradient id="shadowBack" cx="50%" cy="50%" r="50%">
          <stop offset="0" stop-color="#5c8c16"/>
          <stop offset="0.6" stop-color="#a9cf3e"/>
          <stop offset="1" stop-color="#ffffff" stop-opacity="0"/>
        </radialGradient>
      </defs>
      <ellipse cx="106" cy="17" rx="106" ry="17" fill="url(#shadowBack)"/>
    </svg>

    <h2 class="brand-name">CLOVERTON</h2>
    <p class="brand-subtitle"><span class="brand-subtitle__name">CLOVERTON</span> Adoption Center</p>

    <div class="person">
      <p class="person__name">MAREN HOLLIS</p>
      <p class="person__role">Founder/Director</p>
    </div>

    <p class="contact contact--address">
      <span class="contact__badge" aria-hidden="true">
        <svg width="24" height="22" viewBox="0 0 24 22">
          <path d="M12 1 L23 11 H20 V21 H14.5 V14.5 H9.5 V21 H4 V11 H1 Z" fill="#18b814"/>
        </svg>
      </span>
      <span>912 Birchwood Court, Fernwick Springs,<br>KY 40927</span>
    </p>

    <p class="contact contact--phone">
      <span class="contact__badge" aria-hidden="true">
        <svg width="24" height="20" viewBox="0 0 24 20">
          <path d="M2 7 C2 2 22 2 22 7 L19 9 L16 7 V5.5 C13 4.8 11 4.8 8 5.5 V7 L5 9 Z" fill="#18b814"/>
          <rect x="4" y="10" width="16" height="9" rx="2" fill="#18b814"/>
          <circle cx="12" cy="14.5" r="2.6" fill="#e6f53a"/>
        </svg>
      </span>
      <span>(555) 013-4478</span>
    </p>
  </section>

</body>
</html>
```